Halcott Business Card Design

Photography business needs a logo. I would like to see creative licence on options on 1 & 2 sided. I really like the concept of a fully / partially frosted design. I have already used ArtisanHive for my Logo, so I am looking for the same level of assistance with this project.

Industry/Entity Type

Business

Font styles to use
Serif
Script

Requirements
Must have
• Must Have:
• - These are my contact details
• Name: Ames K Halcott
• Mobile: 5550193827
• email: lenorapaske@fernpost.net

```html
<!DOCTYPE html>
<html lang="en">
<head>
<meta charset="utf-8">
<title>Halcott Business Card Design</title>
<link href="https://fonts.googleapis.com/css2?family=Open+Sans:wght@400;700&display=swap" rel="stylesheet">
<style>
  :root {
    --stage: #2a2b2e;
    --card-front: #ffffff;
    --card-back: #f1f1f1;
    --ink: #2b2b2b;
    --accent: #2f86c9;
    --brand: #3b3f9e;
  }
  * { box-sizing: border-box; margin: 0; padding: 0; }
  html, body {
    width: 1200px;
    height: 800px;
    overflow: hidden;
    background: var(--stage);
    font-family: "Open Sans", Arial, sans-serif;
  }
  .canvas {
    position: relative;
    width: 1200px;
    height: 800px;
  }
  .card {
    position: absolute;
    width: 540px;
    height: 308px;
    top: 246px;
  }
  .card--front { left: 40px; background: var(--card-front); }
  .card--back { left: 620px; background: var(--card-back); }

  .brand {
    position: absolute;
    display: flex;
    align-items: center;
    gap: 12px;
    color: var(--brand);
    font-weight: 700;
  }
  .brand__dot {
    border-radius: 50%;
    background: var(--brand);
    flex: none;
  }
  .card--front .brand {
    left: 50%;
    top: 50%;
    transform: translate(-50%, -50%);
    font-size: 46px;
  }
  .card--front .brand__dot { width: 30px; height: 30px; }

  .card--back .brand {
    left: 70px;
    top: 118px;
    font-size: 30px;
  }
  .card--back .brand__dot { width: 20px; height: 20px; }

  .holder {
    position: absolute;
    left: 330px;
    top: 70px;
  }
  .holder__name {
    font-size: 15px;
    font-weight: 700;
    color: var(--ink);
    line-height: 1.2;
  }
  .holder__role {
    font-size: 10px;
    color: var(--accent);
  }
  .contact {
    position: absolute;
    display: flex;
    align-items: center;
    gap: 12px;
    font-size: 11px;
    color: var(--accent);
  }
  .contact svg { flex: none; }
  .contact--email { left: 312px; top: 176px; }
  .contact--mobile { left: 50px; top: 252px; }
</style>
</head>
<body>
  <main class="canvas">
    <section class="card card--front" aria-label="Card front">
      <div class="brand">
        <span class="brand__dot"></span>
        <span class="brand__name">Halcott</span>
      </div>
    </section>

    <section class="card card--back" aria-label="Card back">
      <div class="brand">
        <span class="brand__dot"></span>
        <span class="brand__name">Halcott</span>
      </div>

      <div class="holder">
        <p class="holder__name">Ames K Halcott</p>
        <p class="holder__role">Photo Manager</p>
      </div>

      <p class="contact contact--email">
        <svg width="14" height="10" viewBox="0 0 14 10" aria-hidden="true">
          <rect x="0" y="0" width="14" height="10" fill="#2b2b2b"/>
          <path d="M0 0 L7 6 L14 0" fill="none" stroke="#f1f1f1" stroke-width="1.2"/>
        </svg>
        <span>Email: lenorapaske@fernpost.net</span>
      </p>

      <p class="contact contact--mobile">
        <svg width="9" height="14" viewBox="0 0 9 14" aria-hidden="true">
          <rect x="0.6" y="0.6" width="7.8" height="12.8" rx="1.2" fill="none" stroke="#2b2b2b" stroke-width="1.2"/>
          <rect x="3" y="11" width="3" height="1" fill="#2b2b2b"/>
        </svg>
        <span>Mobile: 5550193827</span>
      </p>
    </section>
  </main>
</body>
</html>
```